Marketing company needs business card design

Our company (Ventures Beyond Harbor) need a business card design for a marketing company. The design should of course include the logo and business colors (orange and blue). I would like the design to be clean and professional. The business card is going to be a die cut card that is leaf shaped (I have uploaded the template for it). I would love to see a design that is professional but nothing too "corporate."
Updates

Hello everyone,

Just wanted to let you know that I have uploaded an AI and EPS version of the logo for your convenience.

Thank you!

~Marlene

Industry/Entity Type

Marketing

Requirements
Must have
• Must have the following contact info:

Ventures Beyond Harbor
2817 Hollow Brook Ln B204
Prescott, AZ 86517

928.471.6083

info@venturesbeyondharbor-example.com

```html
<!DOCTYPE html>
<html lang="en">
<head>
<meta charset="utf-8">
<title>Ventures Beyond Harbor – Business Card</title>
<link rel="stylesheet" href="https://fonts.googleapis.com/css2?family=Lato:wght@400;700&display=swap">
<style>
  :root {
    --backdrop: #d9d9d9;
    --brand-blue: #1aa0e0;
    --brand-blue-deep: #0f8fd3;
    --brand-orange: #eea24a;
    --card-white: #ffffff;
    --shadow: rgba(0, 0, 0, 0.22);
  }
  * { box-sizing: border-box; margin: 0; padding: 0; }
  html, body {
    width: 1200px;
    height: 900px;
    overflow: hidden;
    background: var(--backdrop);
    font-family: "Lato", Arial, sans-serif;
  }
  .canvas {
    position: relative;
    width: 1200px;
    height: 900px;
  }
  .card {
    position: absolute;
    width: 620px;
    height: 354px;
    border-radius: 0 96px 14px 96px;
    box-shadow: 0 10px 26px var(--shadow);
    overflow: hidden;
  }
  /* Back side */
  .card--back {
    left: 110px;
    top: 60px;
    background: var(--brand-blue);
    display: flex;
    align-items: center;
    justify-content: center;
    gap: 18px;
  }
  .brand-dot {
    width: 26px;
    height: 26px;
    border-radius: 50%;
    background: var(--brand-orange);
    flex: none;
  }
  .card--back .brand-name {
    color: var(--card-white);
    font-weight: 700;
    font-size: 40px;
    letter-spacing: 0.2px;
  }
  /* Front side */
  .card--front {
    left: 470px;
    top: 480px;
    background: var(--card-white);
    padding: 44px 44px 0 0;
    text-align: right;
  }
  .card--front .brand-name {
    color: var(--brand-blue-deep);
    font-weight: 700;
    font-size: 32px;
    line-height: 1.1;
  }
  .holder {
    margin-top: 40px;
    font-size: 25px;
    color: var(--brand-blue-deep);
  }
  .holder .divider { color: var(--brand-orange); margin: 0 4px; }
  .holder .role {
    color: var(--brand-orange);
    text-transform: uppercase;
    letter-spacing: 0.5px;
  }
  .contact {
    margin-top: 34px;
    font-size: 17px;
    line-height: 1.3;
    color: var(--brand-blue-deep);
  }
  .contact .web { font-weight: 700; }
  .rule {
    height: 2px;
    background: var(--brand-orange);
    margin: 8px 0 8px 150px;
  }
  .address {
    font-size: 17px;
    color: var(--brand-blue-deep);
  }
</style>
</head>
<body>
  <main class="canvas">
    <section class="card card--back" aria-label="Card back">
      <span class="brand-dot"></span>
      <span class="brand-name">Ventures Beyond Harbor</span>
    </section>

    <section class="card card--front" aria-label="Card front">
      <div class="brand-name">Ventures Beyond Harbor</div>
      <p class="holder">Marlene Whitfield<span class="divider">|</span><span class="role">Owner</span></p>
      <div class="contact">
        <p class="phone">928.471.6083</p>
        <p class="email">info@venturesbeyondharbor-example.com</p>
        <p class="web">www.venturesbeyondharbor-example.com</p>
      </div>
      <div class="rule"></div>
      <p class="address">2817 Hollow Brook Ln B204, Prescott, AZ 86517</p>
    </section>
  </main>
</body>
</html>
```